Wordpress Design - Accounting Practice Startup

We are a relatively new Accounting Firm in Sydney with a primary focus on the Not-For-Profit sector. We need a complete re-design of our wordpress based website: www.larkmoorledgers.com.au
We already have a logo design which we would like to keep using. See uploaded files.
We have a simple menu stucture:
- Home
- About Us
- Our Services
- Contact Us
(Suggestions welcome!)
Happy for it to be a single page scrolling website linked via the menu. We would like the "Our Services" page/section to have icons for the following:
- Bookkeeping
- Payroll
- Accounting
- Training
- Consulting
- Projects
We'd like a banner at the top of the page below the menu, and a place for testimonials, possibly integrated into the body or to the side. Images and icons to be included would be great.
Our main aim is to have an elegant and modern website that works well on all devices.
Industry/Entity Type
Accounting
Colors
Designer to choose colors to be used in the design.
Look and feel
Each slider illustrates characteristics of the customer's brand and the style your logo design should communicate.

```html
<!DOCTYPE html>
<html lang="en">
<head>
<meta charset="utf-8">
<title>Larkmoor Ledgers</title>
<link href="https://fonts.googleapis.com/css2?family=Fira+Sans+Condensed:wght@500;600&family=Lato:ital,wght@0,300;0,400;0,700;1,400&display=swap" rel="stylesheet">
<style>
:root{
  --green:#3d9b35;
  --green-light:#a9d2a3;
  --dark:#2e2e2e;
  --topbar:#333333;
  --grey-bg:#eeeeee;
  --text:#555555;
  --white:#ffffff;
}
*{margin:0;padding:0;box-sizing:border-box}
html,body{width:1200px;height:2903px;overflow:hidden}
body{position:relative;background:var(--white);font-family:"Lato",sans-serif;color:var(--text)}
.abs{position:absolute}
.head{font-family:"Fira Sans Condensed",sans-serif;font-weight:600}
.topbar{left:0;top:0;width:1200px;height:43px;background:var(--topbar)}
.call-btn{left:912px;top:0;width:210px;height:50px;background:var(--green);color:var(--white);font:700 21px "Lato",sans-serif;display:flex;align-items:center;justify-content:center;border-radius:0 0 4px 4px}
.brand{left:77px;top:66px;display:flex;align-items:center;gap:14px}
.brand-mark{width:22px;height:22px;background:var(--green)}
.brand-name{font:300 36px/1 "Lato",sans-serif;color:#333;letter-spacing:1px}
.nav{top:90px;font:400 17px "Lato",sans-serif;color:#555}
.nav.active{color:var(--green)}
.hero{left:0;top:155px;width:1200px;height:640px;background:linear-gradient(135deg,#6d6d6d,#b5b5b5 45%,#7a7a7a)}
.hero-title{left:0;top:355px;width:1200px;text-align:center;color:var(--white);font-size:78px;font-weight:500}
.hero-btn{left:503px;top:470px;width:194px;height:62px;background:var(--white);color:var(--green);font-size:24px;display:flex;align-items:center;justify-content:center}
.section-title{left:0;width:1200px;text-align:center;color:var(--green);font-size:50px}
.about-text{left:193px;top:918px;width:814px;text-align:center;font-size:15px;line-height:25px}
.svc-title{font-size:24px;color:var(--white)}
.svc-text{font-size:14px;line-height:25px;color:#bdbdbd;width:330px}
.svc-left{text-align:right}
.circle{width:104px;height:104px;border-radius:50%;background:var(--green);display:flex;align-items:center;justify-content:center}
.circle.on{background:var(--white);border:3px solid var(--green)}
.quote{left:333px;top:1867px;width:700px;font:italic 14px/25px "Lato",sans-serif;color:#555}
.client{left:333px;top:1950px;font-size:20px;color:#555}
.team-name{font-size:24px;color:var(--green);font-weight:500}
.team-text{font-size:16px;line-height:25px;color:#666;width:300px}
.more{font-size:16px;color:var(--green);text-decoration:underline}
.footer{left:0;top:2409px;width:1200px;height:431px;background:linear-gradient(160deg,#1d2836,#0e1621 60%,#2c3a2a)}
.f-head{font-size:28px;color:var(--white);font-weight:500}
.f-name{font:700 18px "Lato",sans-serif;color:var(--white)}
.f-role{font-size:15px;color:var(--white)}
.f-line{font-size:15px;color:var(--white);display:flex;align-items:center;gap:14px}
.email-input{left:790px;top:2674px;width:259px;height:39px;border:1px solid #3a4350;background:#0c131c;color:#bbb;font:italic 14px "Lato",sans-serif;padding-left:16px;display:flex;align-items:center}
.subscribe{left:790px;top:2726px;width:135px;height:41px;background:var(--green);color:var(--white);font-size:20px;display:flex;align-items:center;justify-content:center}
.bottombar{left:0;top:2840px;width:1200px;height:63px;background:var(--green)}
.copy{left:79px;top:2862px;font-size:15px;color:var(--white)}
.social{top:2850px;width:46px;height:46px;border-radius:50%;background:rgba(255,255,255,.35)}
.social.first{background:var(--white)}
</style>
</head>
<body>

<div class="abs topbar"></div>
<div class="abs call-btn">CALL US NOW</div>

<div class="abs brand"><span class="brand-mark"></span><span class="brand-name">LARKMOOR<br>LEDGERS</span></div>
<span class="abs nav active" style="left:691px">HOME</span>
<span class="abs nav" style="left:780px">ABOUT US</span>
<span class="abs nav" style="left:902px">SERVICES</span>
<span class="abs nav" style="left:1014px">CONTACT US</span>

<div class="abs hero" role="img" aria-label="Photo of a hand using a calculator beside a laptop"></div>
<svg class="abs" style="left:0;top:640px" width="1200" height="160" viewBox="0 0 1200 160">
  <polygon points="0,8 600,150 1200,8 1200,160 0,160" fill="var(--green)"/>
  <polygon points="0,16 600,158 1200,16 1200,160 0,160" fill="#fff"/>
  <polygon points="0,0 600,150 1200,0 1200,8 600,158 0,8" fill="none"/>
</svg>
<div class="abs hero-title head">“every number counts…”</div>
<div class="abs hero-btn head">CONTACT US</div>

<div class="abs section-title head" style="top:845px">ABOUT LARKMOOR LEDGERS</div>
<p class="abs about-text">Larkmoor Ledgers originated with the idea of providing accounting services that would make clients feel safe and find refuge, feel confident that they could trust the numbers in their financial reports. The founders of Larkmoor Ledgers migrated to Australia as refugees and the name of the business alludes to these origins. We strongly believe that every number counts...</p>

<svg class="abs" style="left:0;top:1070px" width="1200" height="650" viewBox="0 0 1200 650">
  <defs>
    <radialGradient id="svcGlow" cx="50%" cy="40%" r="60%">
      <stop offset="0" stop-color="#6a6a6a"/><stop offset="1" stop-color="#2a2a2a"/>
    </radialGradient>
  </defs>
  <polygon points="0,62 600,4 1200,52 1200,646 600,588 0,646" fill="url(#svcGlow)"/>
  <polygon points="600,4 1200,40 1200,52" fill="var(--green)"/>
  <polygon points="0,646 600,588 0,630" fill="var(--green)"/>
</svg>
<div class="abs section-title head" style="top:1130px;color:var(--white);font-size:46px">OUR SERVICES</div>

<div class="abs circle on" style="left:463px;top:1216px"><svg width="44" height="44" viewBox="0 0 44 44" fill="none" stroke="var(--green)" stroke-width="3"><rect x="6" y="10" width="24" height="28"/><rect x="14" y="4" width="24" height="28" fill="#fff"/><line x1="19" y1="12" x2="33" y2="12"/><line x1="19" y1="19" x2="33" y2="19"/><line x1="19" y1="26" x2="33" y2="26"/></svg></div>
<div class="abs circle" style="left:463px;top:1355px"><svg width="44" height="44" viewBox="0 0 44 44" fill="none" stroke="#fff" stroke-width="3"><rect x="8" y="8" width="22" height="30"/><rect x="14" y="4" width="22" height="30" fill="var(--green)"/><text x="20" y="26" fill="#fff" stroke="none" font-size="14" font-family="Lato,sans-serif" font-weight="700">$</text></svg></div>
<div class="abs circle" style="left:463px;top:1490px"><svg width="44" height="44" viewBox="0 0 44 44" fill="none" stroke="#fff" stroke-width="3"><rect x="6" y="8" width="32" height="30" rx="3"/><line x1="6" y1="16" x2="38" y2="16"/><rect x="11" y="21" width="6" height="5"/><rect x="20" y="21" width="6" height="5"/><rect x="29" y="21" width="4" height="12"/><rect x="11" y="29" width="6" height="5"/><rect x="20" y="29" width="6" height="5"/></svg></div>
<div class="abs circle" style="left:633px;top:1216px"><svg width="44" height="44" viewBox="0 0 44 44" fill="none" stroke="#fff" stroke-width="3"><circle cx="11" cy="12" r="4"/><path d="M6 38V22h10v16"/><rect x="20" y="8" width="18" height="16"/><polyline points="24,20 28,15 31,18 35,12"/><line x1="29" y1="24" x2="29" y2="36"/></svg></div>
<div class="abs circle" style="left:633px;top:1355px"><svg width="44" height="44" viewBox="0 0 44 44" fill="#fff"><circle cx="10" cy="10" r="4"/><circle cx="22" cy="10" r="4"/><circle cx="34" cy="10" r="4"/><rect x="6" y="16" width="8" height="12"/><rect x="18" y="16" width="8" height="12"/><rect x="30" y="16" width="8" height="12"/><rect x="8" y="30" width="28" height="4"/><rect x="20" y="34" width="4" height="6"/></svg></div>
<div class="abs circle" style="left:633px;top:1490px"><svg width="44" height="44" viewBox="0 0 44 44" fill="none" stroke="#fff" stroke-width="3"><rect x="8" y="8" width="26" height="32" rx="2"/><rect x="15" y="4" width="12" height="7" fill="var(--green)"/><polyline points="14,24 20,30 30,18"/></svg></div>

<div class="abs svc-left" style="left:110px;top:1222px;width:330px"><div class="svc-title head">Bookkeeping</div><div class="svc-text">Lorem Ipsum is simply dummy text of the printing and typesetting industry.</div></div>
<div class="abs svc-left" style="left:110px;top:1367px;width:330px"><div class="svc-title head">Payroll</div><div class="svc-text">Lorem Ipsum is simply dummy text of the printing and typesetting industry.</div></div>
<div class="abs svc-left" style="left:110px;top:1506px;width:330px"><div class="svc-title head">Accounting</div><div class="svc-text" style="margin-left:30px;width:300px">Lorem Ipsum is simply dummy text of the printing and typesetting industry.</div></div>
<div class="abs" style="left:755px;top:1222px"><div class="svc-title head">Training</div><div class="svc-text">Lorem Ipsum is simply dummy text of the printing and typesetting industry.</div></div>
<div class="abs" style="left:755px;top:1367px"><div class="svc-title head">Consulting</div><div class="svc-text">Lorem Ipsum is simply dummy text of the printing and typesetting industry.</div></div>
<div class="abs" style="left:755px;top:1506px"><div class="svc-title head">Projects</div><div class="svc-text">Lorem Ipsum is simply dummy text of the printing and typesetting industry.</div></div>

<div class="abs section-title head" style="top:1748px">TESTIMONIALS</div>
<svg class="abs" style="left:116px;top:1892px" width="20" height="48" viewBox="0 0 20 48"><polyline points="17,2 3,24 17,46" fill="none" stroke="var(--green)" stroke-width="2"/></svg>
<svg class="abs" style="left:1052px;top:1892px" width="20" height="48" viewBox="0 0 20 48"><polyline points="3,2 17,24 3,46" fill="none" stroke="var(--green)" stroke-width="2"/></svg>
<div class="abs head" style="left:158px;top:1820px;font-size:110px;line-height:1;color:var(--green-light)">“</div>
<div class="abs head" style="left:570px;top:1920px;font-size:110px;line-height:1;color:var(--green-light)">”</div>
<div class="abs" style="left:196px;top:1869px;width:112px;height:112px;border-radius:50%;background:linear-gradient(#d8d8d8,#b9c0c8)" role="img" aria-label="Client portrait"></div>
<p class="abs quote">"Lorem Ipsum is simply dummy text of the printing and typesetting industry. Lorem Ipsum has been the industry's standard dummy text ever since the 1500s, when an unknown printer took a galley of type and scrambled."</p>
<div class="abs client">- Client Name</div>

<div class="abs" style="left:0;top:2051px;width:1200px;height:370px;background:var(--grey-bg)"></div>
<div class="abs section-title head" style="top:2083px">OUR TEAM</div>
<svg class="abs" style="left:77px;top:2163px" width="155" height="190" viewBox="0 0 155 190" role="img" aria-label="Portrait of Milo Tran"><polygon points="0,0 155,8 155,190 0,182" fill="#c9c9c9"/></svg>
<svg class="abs" style="left:968px;top:2163px" width="155" height="190" viewBox="0 0 155 190" role="img" aria-label="Portrait of Vera Lim"><polygon points="0,8 155,0 155,182 0,190" fill="#d3d3d3"/></svg>
<div class="abs" style="left:261px;top:2182px"><div class="team-name head">Milo Tran, Consultant</div><div class="team-text" style="margin-top:12px">Milo holds a Bachelor of Engineering majoring in Computer Systems with First Class Honours, with the Harbour Institute of Technology.</div><div class="more" style="margin-top:8px">READ MORE</div></div>
<div class="abs" style="left:648px;top:2182px"><div class="team-name head">Vera Lim, Principal Consultant</div><div class="team-text" style="margin-top:12px">Vera is a Chartered Accountant with a strong passion for working with non-profit organisations. Vera holds a degree in Commerce.</div><div class="more" style="margin-top:8px">READ MORE</div></div>

<div class="abs footer" role="img" aria-label="City office towers at dusk"></div>
<svg class="abs" style="left:0;top:2405px" width="1200" height="135" viewBox="0 0 1200 135">
  <polygon points="0,0 1200,0 1200,14 600,130 0,14" fill="var(--green)"/>
  <polygon points="0,0 1200,0 1200,4 600,120 0,4" fill="var(--grey-bg)"/>
</svg>

<div class="abs f-head head" style="left:79px;top:2604px">CONTACT INFO</div>
<div class="abs f-name" style="left:108px;top:2661px">Vera Lim</div>
<div class="abs f-role" style="left:108px;top:2688px">Principal Consultant</div>
<div class="abs f-line" style="left:79px;top:2720px"><svg width="16" height="16" viewBox="0 0 16 16"><path d="M3 1l3 3-2 2c1 2 3 4 5 5l2-2 3 3-2 3C7 15 1 9 1 3z" fill="var(--green)"/></svg>0491 570 156</div>
<div class="abs f-line" style="left:79px;top:2752px"><svg width="16" height="12" viewBox="0 0 16 12" fill="none" stroke="var(--green)" stroke-width="1.6"><rect x="1" y="1" width="14" height="10"/><polyline points="1,1 8,7 15,1"/></svg>vera@larkmoorledgers.com.au</div>

<div class="abs f-head head" style="left:437px;top:2604px">CONTACT INFO</div>
<div class="abs f-name" style="left:466px;top:2661px">Milo Tran</div>
<div class="abs f-role" style="left:466px;top:2688px">Consultant</div>
<div class="abs f-line" style="left:437px;top:2720px"><svg width="16" height="16" viewBox="0 0 16 16"><path d="M3 1l3 3-2 2c1 2 3 4 5 5l2-2 3 3-2 3C7 15 1 9 1 3z" fill="var(--green)"/></svg>0491 570 159</div>
<div class="abs f-line" style="left:437px;top:2752px"><svg width="16" height="12" viewBox="0 0 16 12" fill="none" stroke="var(--green)" stroke-width="1.6"><rect x="1" y="1" width="14" height="10"/><polyline points="1,1 8,7 15,1"/></svg>milo@larkmoorledgers.com.au</div>

<div class="abs f-head head" style="left:790px;top:2604px">NEWSLETTER</div>
<div class="abs email-input">Enter Email</div>
<div class="abs subscribe head">SUBSCRIBE</div>

<div class="abs bottombar"></div>
<div class="abs copy">2017 ©LARKMOOR LEDGERS - All Rights Reserved.</div>
<div class="abs social first" style="left:906px"></div>
<div class="abs social" style="left:962px"></div>
<div class="abs social" style="left:1018px"></div>
<div class="abs social" style="left:1074px"></div>

</body>
</html>
```